Business Card Design

We are looking for a double sided business card.

On one side would be our logo

On the Other Side

Martin Kolby
Sales and Marketing

Phone/Text Logo and 530-418-2763
Email Logo and info@plumvalepets.com
Website Logo and www.plumvalepets.com
Facebook Logo and plumvale pets
Instagram Logo and plumvale_pets

Target Market(s)

Pet owners

Contact Information for Business Card

In project description

Requirements
Must have
• Logo

```html
<!DOCTYPE html>
<html lang="en">
<head>
<meta charset="UTF-8">
<title>Plumvale Pets – Business Card</title>
<link href="https://fonts.googleapis.com/css2?family=Poppins:wght@400;500;600&display=swap" rel="stylesheet">
<style>
  :root {
    --stage: #2a2a2a;
    --card-black: #050505;
    --orange: #f0962a;
    --orange-deep: #e8792c;
    --yellow: #f2c12e;
    --silver: #d9d9d9;
    --white: #ffffff;
    --ink: #111111;
  }
  * { box-sizing: border-box; margin: 0; padding: 0; }
  html, body {
    width: 1200px; height: 1015px; overflow: hidden;
    background: var(--stage);
    font-family: "Poppins", sans-serif;
  }
  .canvas {
    width: 1200px; height: 1015px;
    display: flex; flex-direction: column; align-items: center; justify-content: center;
    gap: 34px;
  }
  .card {
    position: relative;
    width: 800px; height: 457px;
    background: var(--card-black);
    overflow: hidden;
    box-shadow: 0 10px 30px rgba(0,0,0,.5);
  }

  /* Logo side */
  .card-back {
    display: flex; flex-direction: column; align-items: center; justify-content: center;
  }
  .brand { display: flex; align-items: center; gap: 16px; }
  .brand-dot {
    width: 34px; height: 34px; border-radius: 50%;
    background: var(--orange);
  }
  .brand-name {
    font-weight: 600; font-size: 58px; letter-spacing: 3px;
    color: var(--silver); text-transform: uppercase;
  }
  .back-web {
    margin-top: 14px;
    font-size: 15px; letter-spacing: 6px; text-transform: uppercase;
    color: var(--orange);
  }
  .socials {
    margin-top: 40px; display: flex; gap: 48px;
    font-size: 24px; color: var(--white);
  }
  .social { display: flex; align-items: center; gap: 10px; }
  .social-mark { width: 14px; height: 14px; background: var(--orange); }
  .social-mark.round { border-radius: 50%; }
  .social-mark.square { border-radius: 3px; }

  /* Details side */
  .card-front svg.artwork { position: absolute; inset: 0; }
  .front-brand {
    position: absolute; right: 44px; top: 46px;
    display: flex; align-items: center; gap: 10px;
  }
  .front-brand .brand-dot { width: 22px; height: 22px; }
  .front-brand .brand-name { font-size: 38px; letter-spacing: 2px; }
  .person { position: absolute; left: 52px; top: 96px; }
  .person-name {
    font-weight: 500; font-size: 30px; color: var(--orange);
    text-transform: uppercase; letter-spacing: 1px; line-height: 1.1;
  }
  .person-role { font-size: 25px; color: var(--white); line-height: 1.2; }
  .contacts {
    position: absolute; left: 150px; bottom: 36px;
    list-style: none; color: var(--ink); font-size: 24px; line-height: 1.28;
  }
  .contacts li { display: flex; align-items: center; gap: 12px; }
  .contacts svg { width: 20px; height: 20px; flex: none; }
</style>
</head>
<body>
<main class="canvas">

  <section class="card card-back" aria-label="Business card, logo side">
    <div class="brand">
      <span class="brand-dot"></span>
      <span class="brand-name">Plumvale Pets</span>
    </div>
    <p class="back-web">www.plumvalepets.com</p>
    <div class="socials">
      <span class="social"><span class="social-mark round"></span>plumvale pets</span>
      <span class="social"><span class="social-mark square"></span>plumvale_pets</span>
    </div>
  </section>

  <section class="card card-front" aria-label="Business card, contact side">
    <svg class="artwork" viewBox="0 0 800 457" width="800" height="457">
      <defs>
        <linearGradient id="band-fill" x1="0" y1="1" x2="1" y2="0">
          <stop offset="0" stop-color="#f2b22e"/>
          <stop offset="1" stop-color="#ee8f2a"/>
        </linearGradient>
      </defs>
      <path class="illustration-band" role="img"
            aria-label="Area for a double helix illustration in orange, yellow and silver"
            fill="url(#band-fill)"
            d="M0 250 C200 290 520 190 800 150 L800 457 L0 457 Z"/>
    </svg>

    <div class="front-brand">
      <span class="brand-dot"></span>
      <span class="brand-name">Plumvale Pets</span>
    </div>

    <div class="person">
      <p class="person-name">Martin Kolby</p>
      <p class="person-role">Sales and Marketing</p>
    </div>

    <ul class="contacts">
      <li>
        <svg viewBox="0 0 24 24" aria-hidden="true"><path fill="#111" d="M6.6 10.8a15 15 0 0 0 6.6 6.6l2.2-2.2c.3-.3.7-.4 1-.2 1.1.4 2.3.6 3.6.6.6 0 1 .4 1 1V20c0 .6-.4 1-1 1A17 17 0 0 1 3 4c0-.6.4-1 1-1h3.5c.6 0 1 .4 1 1 0 1.3.2 2.5.6 3.6.1.3 0 .7-.2 1z"/></svg>
        530-418-2763
      </li>
      <li>
        <svg viewBox="0 0 24 24" aria-hidden="true"><rect x="2" y="5" width="20" height="14" rx="1" fill="#111"/><path d="M3 6l9 7 9-7" stroke="#f2b22e" stroke-width="1.6" fill="none"/></svg>
        info@plumvalepets.com
      </li>
      <li>
        <svg viewBox="0 0 24 24" aria-hidden="true"><g fill="none" stroke="#111" stroke-width="1.8"><circle cx="12" cy="12" r="9"/><ellipse cx="12" cy="12" rx="4" ry="9"/><path d="M3 12h18M5 7h14M5 17h14"/></g></svg>
        www.plumvalepets.com
      </li>
    </ul>
  </section>

</main>
</body>
</html>
```